Delcourt Realty Business Cards

Design business card

Target Market(s)

High-End Buyer of Real Estate over $1 million dollars

Industry/Entity Type

Realtor

Contact Information for Business Card

Lena Delcourt R(S) LIC.# 41972
Cell 555 246-1938
Email Lena@Delcourt.example
Website IsleFreshHomes.example

Also Need Cards for:

Hank Delcourt R(B) LIC# 69418
C 555 613-7052
E Hank@Delcourt.example
W IsleFreshHomes.example

Colors

Designer to choose colors to be used in the design.

Requirements
Must have
• Address on back:
• 287 Pohaku Cir. , Wailea HI 96753
• Logo on back
Nice to have
• I would like the phone numbers and email address to be big so people can read it easily
Should not have
• Very small print Except For: address (287 Pohaku Cir. Kaleo Bay HI 96700)

```html
<!DOCTYPE html>
<html lang="en">
<head>
<meta charset="utf-8">
<title>Delcourt Realty Business Cards</title>
<link href="https://fonts.googleapis.com/css2?family=Lato:wght@400;700&display=swap" rel="stylesheet">
<style>
  :root {
    --page: #e4e6e8;
    --ink: #262b35;
    --band-light: #3a404c;
    --white: #ffffff;
    --muted: #c5cad2;
    --accent: #e0a02a;
    --name: #2b2f37;
  }
  * { margin: 0; padding: 0; box-sizing: border-box; }
  html, body { width: 1200px; height: 1200px; overflow: hidden; }
  body {
    background: var(--page);
    font-family: "Lato", sans-serif;
    position: relative;
  }
  .card {
    position: absolute;
    left: 224px;
    width: 756px;
    height: 432px;
    border-radius: 18px;
    overflow: hidden;
    box-shadow: 0 10px 30px rgba(0,0,0,0.12);
  }
  .card-front { top: 110px; background: var(--white); }
  .card-back { top: 658px; background: var(--ink); }

  .brand-lockup {
    position: absolute;
    left: 346px;
    top: 44px;
    height: 90px;
    display: flex;
    align-items: center;
    gap: 14px;
  }
  .brand-square { width: 22px; height: 22px; background: var(--ink); border-radius: 3px; }
  .brand-name {
    font-weight: 700;
    font-size: 27px;
    line-height: 1.12;
    letter-spacing: 3px;
    color: var(--ink);
    text-transform: uppercase;
  }
  .team-photo {
    position: absolute;
    left: 610px;
    top: 40px;
    width: 120px;
    height: 93px;
    background: linear-gradient(90deg, #e8b9a4 0%, #c9463f 35%, #f3efe9 60%, #232428 100%);
  }

  .agent { position: absolute; top: 202px; }
  .agent-lena { left: 62px; }
  .agent-hank { left: 468px; }
  .agent-name { font-size: 29px; font-weight: 400; color: var(--name); }
  .agent-license { margin-top: 8px; font-size: 16px; color: var(--name); }

  .contact-band {
    position: absolute;
    left: 0; right: 0; bottom: 0;
    height: 146px;
    background: var(--ink);
  }
  .contact-list { position: absolute; top: 34px; list-style: none; }
  .contact-list.lena { left: 63px; }
  .contact-list.hank { left: 469px; }
  .contact-list li {
    display: flex;
    align-items: center;
    gap: 11px;
    height: 26.5px;
    font-size: 18px;
    letter-spacing: 0.5px;
    color: var(--muted);
  }
  .contact-icon { width: 21px; height: 21px; flex: none; }

  .back-rule {
    position: absolute;
    top: 191px;
    height: 3px;
    background: var(--accent);
  }
  .back-rule.left { left: 0; width: 241px; }
  .back-rule.right { right: 0; width: 236px; }
  .back-brand {
    position: absolute;
    left: 245px;
    top: 148px;
    width: 270px;
    height: 90px;
    display: flex;
    align-items: center;
    justify-content: center;
    gap: 14px;
  }
  .back-brand .brand-square { background: var(--white); }
  .back-brand .brand-name { color: var(--white); }
  .address-band {
    position: absolute;
    left: 0; right: 0; bottom: 0;
    height: 93px;
    background: var(--band-light);
    display: flex;
    align-items: center;
    justify-content: center;
    font-weight: 700;
    font-size: 16px;
    letter-spacing: 0.6px;
    color: var(--white);
  }
</style>
</head>
<body>
  <svg width="0" height="0" style="position:absolute">
    <defs>
      <symbol id="icon-phone" viewBox="0 0 20 20">
        <circle cx="10" cy="10" r="10" fill="#ffffff"/>
        <path d="M6 8.5c0-1.2 1.8-2 4-2s4 .8 4 2l-1.3.4-.4-1.2H7.7l-.4 1.2z M7 9.3h6l.8 4H6.2z" fill="#e0a02a"/>
      </symbol>
      <symbol id="icon-mail" viewBox="0 0 20 20">
        <circle cx="10" cy="10" r="10" fill="#ffffff"/>
        <rect x="5.5" y="6.8" width="9" height="6.4" rx="0.8" fill="#e0a02a"/>
        <path d="M5.8 7.2 10 10.2l4.2-3" stroke="#ffffff" stroke-width="0.9" fill="none"/>
      </symbol>
      <symbol id="icon-web" viewBox="0 0 20 20">
        <circle cx="10" cy="10" r="10" fill="#ffffff"/>
        <circle cx="10" cy="10" r="4.4" fill="#e0a02a"/>
        <path d="M5.8 10h8.4M10 5.8c-1.6 2.6-1.6 5.8 0 8.4M10 5.8c1.6 2.6 1.6 5.8 0 8.4" stroke="#ffffff" stroke-width="0.7" fill="none"/>
      </symbol>
    </defs>
  </svg>

  <section class="card card-front">
    <div class="brand-lockup">
      <span class="brand-square"></span>
      <span class="brand-name">Delcourt<br>Realty</span>
    </div>
    <div class="team-photo" role="img" aria-label="Portrait photo of agents Lena and Hank Delcourt"></div>

    <div class="agent agent-lena">
      <p class="agent-name">Lena Delcourt</p>
      <p class="agent-license">R(S) LIC.# 41972</p>
    </div>
    <div class="agent agent-hank">
      <p class="agent-name">Hank Delcourt</p>
      <p class="agent-license">R(B) LIC# 69418</p>
    </div>

    <div class="contact-band">
      <ul class="contact-list lena">
        <li><svg class="contact-icon"><use href="#icon-phone"/></svg>555 246-1938</li>
        <li><svg class="contact-icon"><use href="#icon-mail"/></svg>Lena@Delcourt.example</li>
        <li><svg class="contact-icon"><use href="#icon-web"/></svg>IsleFreshHomes.example</li>
      </ul>
      <ul class="contact-list hank">
        <li><svg class="contact-icon"><use href="#icon-phone"/></svg>555 613-7052</li>
        <li><svg class="contact-icon"><use href="#icon-mail"/></svg>Hank@Delcourt.example</li>
        <li><svg class="contact-icon"><use href="#icon-web"/></svg>IsleFreshHomes.example</li>
      </ul>
    </div>
  </section>

  <section class="card card-back">
    <div class="back-rule left"></div>
    <div class="back-rule right"></div>
    <div class="back-brand">
      <span class="brand-square"></span>
      <span class="brand-name">Delcourt<br>Realty</span>
    </div>
    <div class="address-band">287 Pohaku Cir. Kaleo Bay HI 96700</div>
  </section>
</body>
</html>
```